Business card for a new cabinet shop company named Marlowe Cabinets for high end cabinets

Design a business card, thinking dark rich green with colours to speak of high end luxury ie; cream, gold, black possibly

Peter Lindqvar
Director Craftsman
Email: info@marlowecabinets.com.au
Instagram : @marlowe.cabinets

```html
<!DOCTYPE html>
<html lang="en">
<head>
<meta charset="utf-8">
<title>Marlowe Cabinets – Business Card</title>
<link href="https://fonts.googleapis.com/css2?family=Montserrat:wght@400;500;700&display=swap" rel="stylesheet">
<style>
  :root {
    --backdrop: #9a9a9a;
    --card-green: #06402b;
    --mark-area-front: #0a4a33;
    --mark-area-back: #053624;
    --gold: #cfae68;
    --cream-white: #ffffff;
    --emboss-green: #0b4f36;
  }
  html, body {
    margin: 0;
    padding: 0;
    width: 1200px;
    height: 1059px;
    overflow: hidden;
    background: var(--backdrop);
    font-family: "Montserrat", sans-serif;
  }
  .canvas {
    position: relative;
    width: 1200px;
    height: 1059px;
  }
  .card {
    position: absolute;
    background: var(--card-green);
    border-radius: 26px;
    overflow: hidden;
  }
  .card--front {
    left: 256px;
    top: 86px;
    width: 696px;
    height: 397px;
  }
  .card--back {
    left: 254px;
    top: 568px;
    width: 703px;
    height: 401px;
  }

  /* Wordmark: one colour, one weight */
  .wordmark {
    position: absolute;
    margin: 0;
    font-weight: 500;
    line-height: 1;
  }
  .wordmark__name,
  .wordmark__trade {
    display: block;
    white-space: nowrap;
  }
  .wordmark__name {
    text-transform: lowercase;
    letter-spacing: 0.5px;
  }
  .wordmark__trade {
    text-transform: uppercase;
  }
  .card--front .wordmark {
    left: 52px;
    top: 24px;
    color: var(--gold);
  }
  .card--front .wordmark__name { font-size: 72px; }
  .card--front .wordmark__trade {
    font-size: 38px;
    letter-spacing: 13px;
    margin-top: 24px;
    margin-left: 2px;
  }

  .mark-area {
    position: absolute;
    display: block;
  }
  .card--front .mark-area {
    left: 376px;
    top: 128px;
    width: 320px;
    height: 269px;
    background: var(--mark-area-front);
  }

  .contact {
    position: absolute;
    left: 40px;
    top: 214px;
  }
  .contact__name {
    margin: 0;
    color: var(--gold);
    font-weight: 700;
    font-size: 27px;
    line-height: 1.2;
  }
  .contact__role {
    margin: 6px 0 0;
    color: var(--cream-white);
    font-weight: 400;
    font-size: 19px;
  }
  .contact__list {
    list-style: none;
    margin: 20px 0 0;
    padding: 0;
  }
  .contact__item {
    display: flex;
    align-items: center;
    gap: 10px;
    color: var(--cream-white);
    font-size: 19px;
    height: 36px;
  }
  .contact__icon {
    width: 20px;
    height: 20px;
    flex: none;
  }

  .card--back .mark-area {
    left: 122px;
    top: 138px;
    width: 150px;
    height: 126px;
    background: var(--mark-area-back);
  }
  .card--back .wordmark {
    left: 303px;
    top: 132px;
    color: var(--emboss-green);
  }
  .card--back .wordmark__name { font-size: 66px; }
  .card--back .wordmark__trade {
    font-size: 35px;
    letter-spacing: 12px;
    margin-top: 22px;
    margin-left: 2px;
  }
</style>
</head>
<body>
<main class="canvas">
  <section class="card card--front" aria-label="Business card front">
    <h1 class="wordmark">
      <span class="wordmark__name">Marlowe</span>
      <span class="wordmark__trade">Cabinets</span>
    </h1>
    <span class="mark-area" role="img" aria-label="Large brand mark decoration area"></span>
    <div class="contact">
      <p class="contact__name">Peter Lindqvar</p>
      <p class="contact__role">Director Craftsman</p>
      <ul class="contact__list">
        <li class="contact__item">
          <svg class="contact__icon" viewBox="0 0 20 20" aria-hidden="true">
            <rect x="1" y="4" width="18" height="12" fill="var(--gold)"/>
            <polyline points="1,4 10,11 19,4" fill="none" stroke="var(--card-green)" stroke-width="1.6"/>
          </svg>
          info@marlowecabinets.com.au
        </li>
        <li class="contact__item">
          <svg class="contact__icon" viewBox="0 0 20 20" aria-hidden="true">
            <circle cx="10" cy="10" r="8" fill="none" stroke="var(--gold)" stroke-width="2"/>
          </svg>
          @marlowe.cabinets
        </li>
      </ul>
    </div>
  </section>

  <section class="card card--back" aria-label="Business card back">
    <span class="mark-area" role="img" aria-label="Embossed brand mark area"></span>
    <h2 class="wordmark">
      <span class="wordmark__name">Marlowe</span>
      <span class="wordmark__trade">Cabinets</span>
    </h2>
  </section>
</main>
</body>
</html>
```